Pharmacy ad

need 2 pharmacy ads for the phone book. one for Brook Pharmacy and one for Oakvale Care Pharmacy. Dimensions for ad is 4.75in x 4.667 in. please see attached examples of ad uploaded as well logos of each pharmacy

```html
<!DOCTYPE html>
<html lang="en">
<head>
<meta charset="utf-8">
<title>Brook Pharmacy – Directory Ad</title>
<link rel="stylesheet" href="https://fonts.googleapis.com/css2?family=Barlow:ital,wght@0,700;1,500&family=Montserrat:wght@300;500;700;800&display=swap">
<style>
  :root{
    --navy:#1d1a40;
    --green:#8cc63f;
    --green-light:#cfe6a3;
    --green-text:#74b043;
    --blue:#8fcbe2;
    --blue-light:#c9e6f1;
    --white:#ffffff;
  }
  html,body{margin:0;padding:0;overflow:hidden;background:var(--white);}
  .ad{position:relative;width:1200px;height:1180px;overflow:hidden;box-sizing:border-box;border:5px solid var(--navy);font-family:"Montserrat",sans-serif;color:var(--navy);}
  .ad-bg{position:absolute;inset:0;}
  .abs{position:absolute;margin:0;}
  .brand-mark{left:240px;top:48px;width:190px;height:190px;border-radius:50%;background:var(--green);}
  .brand{left:480px;top:36px;width:500px;text-align:center;font-family:"Barlow",sans-serif;font-weight:700;line-height:.95;}
  .brand-name{font-size:80px;letter-spacing:1px;}
  .tagline{left:480px;top:218px;width:500px;text-align:center;font-family:"Barlow",sans-serif;font-style:italic;font-weight:500;font-size:27px;color:var(--green-text);}
  .payment{height:67px;top:306px;background:var(--white);display:flex;align-items:center;justify-content:center;font-weight:800;font-size:20px;color:var(--navy);}
  .discount{top:405px;width:400px;text-align:center;}
  .discount-value{font-size:84px;font-weight:800;letter-spacing:-3px;line-height:1;}
  .discount-label{font-size:29px;font-weight:300;line-height:1.05;text-transform:uppercase;}
  .discount-note{font-size:24px;font-weight:800;line-height:1.05;text-transform:uppercase;}
  .divider-v{width:0;border-left:6px dotted var(--navy);}
  .divider-h{left:44px;width:1075px;top:874px;border-top:6px dotted var(--navy);}
  .features{list-style:none;padding:0;}
  .features li{position:relative;padding-left:25px;font-weight:700;font-size:27px;line-height:1.05;margin-bottom:28px;}
  .features li::before{content:"";position:absolute;left:2px;top:10px;width:10px;height:10px;background:var(--navy);transform:rotate(45deg);}
  .email{left:58px;top:905px;font-size:29px;font-weight:500;}
  .branch{top:950px;}
  .branch-address{font-weight:700;font-size:25px;line-height:1;margin:0 0 2px 32px;position:relative;}
  .branch-address svg{position:absolute;left:-32px;top:0;}
  .branch-note{font-size:20px;font-weight:300;margin-left:32px;}
  .branch-phone{font-weight:700;font-size:26px;margin:12px 0 0;display:flex;align-items:center;gap:10px;}
  .branch-hours{font-weight:800;font-size:26px;line-height:1.2;margin-top:18px;text-transform:uppercase;}
  .branch-divider{left:560px;top:955px;height:183px;border-left:3px solid var(--navy);}
  .social-label{left:1000px;top:976px;font-size:26px;font-weight:500;}
  .social{left:1010px;top:1025px;width:120px;text-align:center;}
  .social-dot{width:96px;height:96px;border-radius:50%;background:var(--navy);margin:0 auto 4px;}
  .social-name{font-size:17px;font-weight:700;}
</style>
</head>
<body>
<main class="ad">
  <svg class="ad-bg" width="1200" height="1180" viewBox="0 0 1200 1180" aria-hidden="true">
    <defs>
      <linearGradient id="sky" x1="0" y1="0" x2="0" y2="1">
        <stop offset="0" stop-color="#b6dcea"/>
        <stop offset="1" stop-color="#8fcbe2"/>
      </linearGradient>
      <radialGradient id="meadow" cx="0.5" cy="0.35" r="0.7">
        <stop offset="0" stop-color="#d3eaa9"/>
        <stop offset="1" stop-color="#82c03c"/>
      </radialGradient>
    </defs>
    <rect width="1200" height="1180" fill="url(#sky)"/>
    <path d="M0 580 Q600 660 1200 580 L1200 1180 L0 1180 Z" fill="url(#meadow)"/>
    <path d="M0 0 H1200 V205 Q600 330 0 205 Z" fill="#ffffff"/>
  </svg>

  <div class="abs brand-mark" role="img" aria-label="Brook Pharmacy symbol"></div>
  <h1 class="abs brand">
    <span class="brand-name">BROOK</span><br>
    <span class="brand-name">PHARMACY</span>
  </h1>
  <p class="abs tagline">We Care About Your Health</p>

  <div class="abs payment" style="left:245px;width:104px;">Vantapay</div>
  <div class="abs payment" style="left:381px;width:105px;">Paycircle</div>
  <div class="abs payment" style="left:514px;width:92px;font-size:17px;">Harborlife</div>
  <div class="abs payment" style="left:631px;width:327px;font-size:26px;">Norvale Insurances</div>

  <section class="abs discount" style="left:8px;">
    <div class="discount-value">10%</div>
    <div class="discount-label">Student<br>Discount</div>
    <div class="discount-note">With valid ID card</div>
  </section>
  <div class="abs divider-v" style="left:410px;top:412px;height:188px;"></div>
  <section class="abs discount" style="left:408px;">
    <div class="discount-value">10%</div>
    <div class="discount-label">Senior Citizen<br>Discount</div>
    <div class="discount-note">For patients 60<br>years and over</div>
  </section>
  <div class="abs divider-v" style="left:801px;top:412px;height:188px;"></div>
  <section class="abs discount" style="left:796px;">
    <div class="discount-value">10%</div>
    <div class="discount-label">Discount<br>on hospital</div>
    <div class="discount-note">Prescriptions</div>
  </section>

  <ul class="abs features" style="left:56px;top:662px;">
    <li>Certified Pharmacists</li>
    <li>Affordable prices</li>
    <li>Brand and Generic<br>Medicines</li>
  </ul>
  <ul class="abs features" style="left:473px;top:662px;">
    <li>Injectables</li>
    <li>Special Orders</li>
    <li>Delivery service</li>
  </ul>
  <ul class="abs features" style="left:825px;top:662px;">
    <li>Blood Pressure and<br>Glucose checks</li>
    <li>Personal care and<br>Beauty Products</li>
  </ul>

  <div class="abs divider-h"></div>
  <p class="abs email">For more inquiries, email us: brookpharmacy@mailnest.com</p>

  <section class="abs branch" style="left:56px;">
    <p class="branch-address"><svg width="22" height="28" viewBox="0 0 22 28" aria-hidden="true"><path d="M11 0a11 11 0 0 0-11 11c0 8 11 17 11 17s11-9 11-17A11 11 0 0 0 11 0zm0 15a4 4 0 1 1 0-8 4 4 0 0 1 0 8z" fill="var(--navy)"/></svg>42 Harbour Lane, Eastport</p>
    <div class="branch-note">(opposite Grace Community Chapel)</div>
    <p class="branch-phone"><svg width="28" height="22" viewBox="0 0 28 22" aria-hidden="true"><path d="M2 7c0-5 24-5 24 0v3h-6V7H8v3H2zM6 11h16l4 11H2z" fill="var(--navy)"/></svg>1 555 210 4417</p>
    <div class="branch-hours">Monday – Friday 10am to 6pm<br>Saturday 10am to 5pm</div>
  </section>

  <div class="abs branch-divider"></div>

  <section class="abs branch" style="left:618px;">
    <p class="branch-address"><svg width="22" height="28" viewBox="0 0 22 28" aria-hidden="true"><path d="M11 0a11 11 0 0 0-11 11c0 8 11 17 11 17s11-9 11-17A11 11 0 0 0 11 0zm0 15a4 4 0 1 1 0-8 4 4 0 0 1 0 8z" fill="var(--navy)"/></svg>Marina Walk, Food Court,<br>Eastport</p>
    <p class="branch-phone"><svg width="28" height="22" viewBox="0 0 28 22" aria-hidden="true"><path d="M2 7c0-5 24-5 24 0v3h-6V7H8v3H2zM6 11h16l4 11H2z" fill="var(--navy)"/></svg>1 555 210 4420</p>
    <div class="branch-hours">Monday – Saturday<br>9am to 5pm</div>
  </section>

  <p class="abs social-label">Visit us on</p>
  <div class="abs social">
    <div class="social-dot"></div>
    <div class="social-name">Socialpage</div>
  </div>
</main>
</body>
</html>
```